Harbor Circuits LLC is a Minneapolis / St Paul and surrounding communities computer repair and service company. It serves residential and small businesses. We work primarily with virus removal, data recovery, system baselines, networking, and new system installation. The site should look clean, professional, and easy to navigate.

This wordpress project must be coded and integrated into a wordpress theme for easy upload and maintenance.
Updates

Designers - Please make sure your design is in a wordpress theme so that It can be uploaded.  

Thank you,

Brent 

Target Market(s)

Residential and Small Business

Industry/Entity Type

Residential

Requirements
Must have
• Site Content
1. Main Page should have photos that scroll across, Business Description, Space to run
“Specials” Ads
a. Intuitive Navigation
2. Additional Pages
a. Blog for Computer Repair Articles
b. Testimonials Page
c. Contact Pages
d. Services Page with the ability to put in pricing
3. The site must be clean and professional.
4. Wordpress Theme

```html
<!DOCTYPE html>
<html lang="en">
<head>
<meta charset="utf-8">
<title>Harbor Circuits LLC</title>
<link rel="stylesheet" href="https://fonts.googleapis.com/css2?family=Open+Sans:wght@400;600&family=Oswald:wght@300;400&family=Tinos:ital,wght@0,400;1,400&display=swap">
<style>
:root{
  --green:#629a2c;
  --green-dark:#4f7f22;
  --header:#383838;
  --bg-top:#2f2f2f;
  --black:#000;
  --white:#fff;
  --frame:#8a8a8a;
  --service:#5a5a5a;
  --body:#555;
  --ink:#111;
  --quote:#656565;
  --btn-grey:#9a9a9a;
  --meta-icon:#2aa0c4;
}
*{margin:0;padding:0;box-sizing:border-box}
html,body{width:1200px;height:900px;overflow:hidden}
body{position:relative;background:var(--black);font-family:"Tinos",serif;color:var(--ink)}
.backdrop{position:absolute;left:0;top:82px;width:1200px;height:328px;background:radial-gradient(ellipse at 50% 30%,#4a4a4a 0%,#343434 55%,#262626 100%)}
.site-header{position:absolute;left:0;top:0;width:1200px;height:82px;background:linear-gradient(#414141,#333);border-bottom:2px solid var(--green)}
.brand{position:absolute;left:116px;top:0;width:356px;height:123px;background:var(--black);display:flex;align-items:center;gap:18px;padding-left:22px}
.brand-mark{width:88px;height:88px;border-radius:50%;background:var(--white);border:6px solid var(--green);flex:none}
.brand-name{font-family:"Oswald",sans-serif;font-weight:400;font-size:30px;line-height:1.05;color:var(--green)}
.main-nav{position:absolute;left:552px;top:30px;display:flex;font-family:"Open Sans",sans-serif;font-weight:600;font-size:13px;color:#d6d6d6}
.main-nav a{color:inherit;text-decoration:none;padding:0 18px;border-right:1px solid #666;line-height:20px}
.main-nav a:last-child{border-right:0}
.slider{position:absolute;left:114px;top:128px;width:979px;height:343px;background:var(--white);border:5px solid var(--frame);border-radius:4px;box-shadow:0 0 18px rgba(0,0,0,.6)}
.slide-photo{position:absolute;left:12px;top:6px;width:478px;height:322px;background:radial-gradient(ellipse at 45% 55%,#6a6a6a 0%,#9a9a9a 45%,#f4f4f4 80%)}
.service-list{position:absolute;left:536px;top:28px;list-style:none;font-family:"Open Sans",sans-serif;font-weight:600;font-size:24px;color:var(--service);letter-spacing:.3px}
.service-list li{display:flex;align-items:center;height:36px}
.service-list svg{width:36px;height:28px;margin-right:18px}
.btn-contact{position:absolute;left:586px;top:227px;width:224px;height:62px;border-radius:8px;border:2px solid var(--green);background:linear-gradient(#4a4a4a,#050505);color:var(--green);font-family:"Oswald",sans-serif;font-size:30px;display:flex;align-items:center;justify-content:center;letter-spacing:-.5px}
.slide-dots{position:absolute;left:832px;top:300px;display:flex;gap:10px}
.slide-dots span{width:21px;height:21px;border-radius:50%;background:var(--black)}
.slide-dots span.active{background:var(--green)}
.content{position:absolute;left:96px;top:488px;width:1014px;height:360px;background:var(--white);border:4px solid var(--green);border-radius:6px}
.col{position:absolute;top:4px}
.col-title{display:flex;align-items:center;gap:8px;font-family:"Oswald",sans-serif;font-weight:300;font-size:33px;color:#333;height:60px}
.badge{width:60px;height:60px;border-radius:50%;background:var(--green);display:flex;align-items:center;justify-content:center}
.about{left:18px;width:280px}
.about .lead{font-size:18px;line-height:22px;margin:8px 0 10px 4px}
.about p{font-size:16px;line-height:20px;color:var(--body);margin:0 0 10px 4px}
.btn-grey{position:absolute;width:136px;height:40px;border-radius:7px;background:var(--btn-grey);box-shadow:0 3px 3px rgba(0,0,0,.25);font-family:"Oswald",sans-serif;font-size:19px;color:#333;display:flex;align-items:center;justify-content:center}
.about .btn-grey{left:140px;top:295px}
.clients{left:341px;width:325px}
.quote{position:relative;margin-top:6px;background:var(--quote);border-radius:8px;padding:30px 10px 18px 39px;color:var(--white);font-style:italic;font-size:16px;line-height:22.5px}
.quote p+p{margin-top:10px}
.quote-mark{position:absolute;left:18px;top:6px;font-size:68px;color:var(--green);font-style:normal;line-height:1}
.quote-tail{position:absolute;left:80px;bottom:-20px}
.cite{text-align:right;margin-top:22px;font-size:19px;line-height:21px;padding-right:18px}
.cite small{display:block;font-size:16px;color:var(--body)}
.blog{left:704px;width:300px}
.post h3{font-weight:400;font-size:18px;line-height:22px;margin-top:6px}
.meta{display:flex;align-items:center;gap:6px;font-size:15px;margin:2px 0 8px -4px}
.meta svg{width:16px;height:16px}
.meta span{margin-right:8px}
.post p{font-size:16px;line-height:20px;color:var(--body);margin-bottom:10px}
.blog .btn-grey{left:139px;top:296px}
.site-footer{position:absolute;left:0;top:860px;width:1200px;height:40px;background:var(--green);font-size:19px;display:flex;align-items:center;justify-content:center;padding-right:90px}
</style>
</head>
<body>
<div class="backdrop"></div>

<header class="site-header">
  <div class="brand">
    <div class="brand-mark"></div>
    <div class="brand-name">Harbor Circuits LLC</div>
  </div>
  <nav class="main-nav">
    <a href="#">Home</a><a href="#">Services</a><a href="#">Pricing</a><a href="#">Blog</a><a href="#">Testimonials</a><a href="#">Contact Us</a>
  </nav>
</header>

<section class="slider">
  <div class="slide-photo" role="img" aria-label="Desktop computer tower with monitor, keyboard and mouse"></div>
  <ul class="service-list">
    <li><svg viewBox="0 0 36 28"><path d="M2 15l10 10L34 3l-4-3-18 17-6-6z" fill="#629a2c"/></svg>VIRUS REMOVAL</li>
    <li><svg viewBox="0 0 36 28"><path d="M2 15l10 10L34 3l-4-3-18 17-6-6z" fill="#629a2c"/></svg>DATA RECOVERY</li>
    <li><svg viewBox="0 0 36 28"><path d="M2 15l10 10L34 3l-4-3-18 17-6-6z" fill="#629a2c"/></svg>SYSTEM BASELINES</li>
    <li><svg viewBox="0 0 36 28"><path d="M2 15l10 10L34 3l-4-3-18 17-6-6z" fill="#629a2c"/></svg>NETWORKING</li>
    <li><svg viewBox="0 0 36 28"><path d="M2 15l10 10L34 3l-4-3-18 17-6-6z" fill="#629a2c"/></svg>NEW SYSTEM INSTALLATION</li>
  </ul>
  <a class="btn-contact">CONTACT NOW</a>
  <div class="slide-dots"><span class="active"></span><span></span><span></span><span></span></div>
</section>

<main class="content">
  <div class="col about">
    <h2 class="col-title">About Us
      <span class="badge"><svg width="38" height="38" viewBox="0 0 38 38"><path d="M6 32L22 16" stroke="#000" stroke-width="6" stroke-linecap="round"/><circle cx="26" cy="11" r="8" fill="#000"/><circle cx="30" cy="7" r="4" fill="#629a2c"/><path d="M8 6l24 26" stroke="#000" stroke-width="5" stroke-linecap="round"/></svg></span>
    </h2>
    <p class="lead" style="color:#111">Lorem ipsum dolor sit amet, consectetuer adipis cing elit mauris.</p>
    <p>Sed laoreet aliquam leo. Ut tellus dolor, dapibus eget, elementum vel, cursus eleifend, elit. Aenean auctor wisi et urna. Aliquam erat volutpat. Duis ac turpis. Integer rutrum ante eu lacus.</p>
    <p>Vestibulum libero nisl, porta vel, scelerisque eget, malesuada at, neque. Vivamus eget nibh. Etiam cursus leo vel</p>
    <a class="btn-grey">KNOW MORE</a>
  </div>

  <div class="col clients">
    <h2 class="col-title">Our Clients Say
      <span class="badge"><svg width="40" height="36" viewBox="0 0 40 36"><circle cx="13" cy="11" r="6" fill="#333"/><circle cx="27" cy="11" r="6" fill="#333"/><path d="M2 34c0-10 6-14 11-14s11 4 11 14z" fill="#333"/><path d="M16 34c0-10 6-14 11-14s11 4 11 14z" fill="#222"/></svg></span>
    </h2>
    <div class="quote">
      <span class="quote-mark">&ldquo;</span>
      <p>Suspendisse sollicitudin velit sed leo. Ut pharetra augue nec augue. Nam elit agna, endrerit sit amet, tincidunt, viverra sed, nulla. Donec porta diam eu massa.</p>
      <p>Quisque diam lorem, interdum vitae, dapibus ac, scelerisque vitae, pede.</p>
      <svg class="quote-tail" width="40" height="22" viewBox="0 0 40 22"><path d="M0 0h40L38 22z" fill="#656565"/></svg>
    </div>
    <div class="cite">Dana Whitfield,<small>Company Name</small></div>
  </div>

  <div class="col blog">
    <h2 class="col-title">From The Blog
      <span class="badge"><svg width="36" height="36" viewBox="0 0 36 36"><circle cx="8" cy="28" r="5" fill="#000"/><path d="M4 14a18 18 0 0 1 18 18" stroke="#000" stroke-width="5" fill="none"/><path d="M4 4a28 28 0 0 1 28 28" stroke="#000" stroke-width="5" fill="none"/></svg></span>
    </h2>
    <article class="post">
      <h3>Ut tellus dolor, dapibus eget, elementum vel, cursus eleifend,</h3>
      <div class="meta">
        <svg viewBox="0 0 16 16"><rect x="1" y="3" width="14" height="12" fill="none" stroke="#2aa0c4" stroke-width="2"/><rect x="1" y="3" width="14" height="4" fill="#2aa0c4"/></svg><span>May 11, 2011</span>
        <svg viewBox="0 0 16 16"><circle cx="8" cy="5" r="4" fill="#2aa0c4"/><path d="M1 16c0-5 3-7 7-7s7 2 7 7z" fill="#2aa0c4"/></svg><span>Admin</span>
        <svg viewBox="0 0 16 16"><path d="M1 2h14v9H6l-4 4v-4H1z" fill="#2aa0c4"/></svg><span>3 Comments</span>
      </div>
      <p>Aliquam erat volutpat. Duis ac turpis. Integer rutrum ante eu lacus.</p>
    </article>
    <article class="post">
      <h3>Aliquam erat volutpat. Duis ac turpis.</h3>
      <div class="meta">
        <svg viewBox="0 0 16 16"><rect x="1" y="3" width="14" height="12" fill="none" stroke="#2aa0c4" stroke-width="2"/><rect x="1" y="3" width="14" height="4" fill="#2aa0c4"/></svg><span>May 11, 2011</span>
        <svg viewBox="0 0 16 16"><circle cx="8" cy="5" r="4" fill="#2aa0c4"/><path d="M1 16c0-5 3-7 7-7s7 2 7 7z" fill="#2aa0c4"/></svg><span>Admin</span>
        <svg viewBox="0 0 16 16"><path d="M1 2h14v9H6l-4 4v-4H1z" fill="#2aa0c4"/></svg><span>3 Comments</span>
      </div>
      <p>Aliquam erat volutpat. Duis ac turpis. Integer rutrum ante eu lacus.</p>
    </article>
    <a class="btn-grey">VIEW ALL POSTS</a>
  </div>
</main>

<footer class="site-footer">Copyrights Reserved@ HarborLLC</footer>
</body>
</html>
```